Homepage layout for online ad network

Attached is our Calvrex Media logo and updated brief (I can't seem to delete the old logo and brief, but they're no longer relevant).

This project was originally posted with a different logo and corporate name, but we have decided to stay with our current logo and name and redesign the site.

Your design is for a homepage only - design, no coding (I'll get someone else to take your PSD and code it).

Your homepage will make use of a Flash slider - BUT YOU ARE NOT REQUIRED TO PROVIDE THE FLASH. Instead, simply provide the layout and at least two static examples out of the four different sections that will eventually be in the slider.

Much of this design is based on the design of a competitor (listed in the brief).

Please ask whatever questions you need to in order to clarify instructions.
Updates

Project updated to include new logo (and correspondingly new color scheme).

Brief changed slightly.

Thank you for submitting designs for this project in the past.

After some internal strategy work, we have decided to retain our initial corporate identity, Calvrex Media.

If you have submitted a design for the original brief and are available, please re-work your best prior design to reflect the color scheme in the newly uploaded logo.

Target Market(s)

This site is aimed primarily at young professionals who buy digital media on behalf of large advertisers.

Industry/Entity Type

Media

Requirements
Must have
• modern white space
Should not have
• no Flash outside of slider

```html
<!DOCTYPE html>
<html lang="en">
<head>
<meta charset="utf-8">
<title>Calvrex Media — Site-Specific Campaigns</title>
<link href="https://fonts.googleapis.com/css2?family=Montserrat:wght@500;600;700&family=Roboto+Condensed:wght@300;400;700&family=Arimo:wght@400;700&display=swap" rel="stylesheet">
<style>
  :root {
    --lime: #d4df27;
    --lime-light: #eef25a;
    --crimson: #c0202f;
    --ink: #222222;
    --text: #333333;
    --rule: #555555;
    --mist: #d2d2d2;
    --slide-bg: #e8ecef;
    --photo: #cfd6dc;
  }
  * { box-sizing: border-box; margin: 0; padding: 0; }
  html, body { width: 1200px; height: 1000px; overflow: hidden; background: #fff; }
  body { position: relative; font-family: 'Arimo', Arial, sans-serif; color: var(--text); }

  .site-header { position: absolute; left: 0; top: 0; width: 1200px; height: 120px; background: #fff; border-bottom: 4px solid var(--lime); }
  .brand { position: absolute; left: 134px; top: 34px; display: flex; align-items: center; gap: 10px;
    font-family: 'Montserrat', sans-serif; font-weight: 600; font-size: 34px; color: var(--ink); letter-spacing: -0.5px; }
  .brand-mark { width: 22px; height: 22px; background: var(--lime); }
  .brand-pointer { position: absolute; left: 253px; top: 101px; width: 0; height: 0;
    border-left: 8px solid transparent; border-right: 8px solid transparent; border-bottom: 14px solid var(--lime); }
  .tagline { position: absolute; right: 116px; top: 14px; font-family: 'Montserrat', sans-serif; font-weight: 600;
    font-size: 13px; color: var(--lime); letter-spacing: 0.2px; }
  .main-nav { position: absolute; right: 116px; top: 68px; display: flex; height: 33px; }
  .main-nav a { display: flex; align-items: center; padding: 0 14px; font-family: 'Montserrat', sans-serif; font-weight: 600;
    font-size: 12.5px; color: var(--ink); text-decoration: none; border-left: 1px solid #ccc; }
  .main-nav a:first-child { border-left: none; }
  .main-nav a.active-sep { border-left-color: var(--lime); }
  .main-nav a:last-child { padding-right: 0; }

  .hero-band { position: absolute; left: 0; top: 120px; width: 1200px; height: 220px; background: linear-gradient(#d0d0d0, #fff); }

  .slider { position: absolute; left: 123px; top: 150px; width: 960px; height: 350px;
    background: linear-gradient(90deg, #dde2e6 0%, #f6f7f8 30%, #e9edf0 60%, #f3f6f8 100%);
    box-shadow: 0 6px 6px rgba(0,0,0,0.45); overflow: hidden; }
  .slide-title { position: absolute; left: 103px; top: 118px; font-family: 'Montserrat', sans-serif; font-weight: 700;
    font-size: 40px; color: #2a2a2a; letter-spacing: 1px; }
  .slide-sub { position: absolute; left: 105px; top: 165px; font-family: 'Montserrat', sans-serif; font-weight: 500;
    font-size: 20px; line-height: 24px; color: var(--crimson); letter-spacing: 0.6px; }
  .slide-photo { position: absolute; left: 592px; top: 5px; width: 225px; height: 345px;
    background: linear-gradient(180deg, #f4f4f4 0%, #e6e8ea 55%, #b9c7a2 75%, #eef0f0 100%); border-radius: 40px 40px 0 0; }
  .slide-arrow { position: absolute; top: 158px; }
  .slide-arrow.prev { left: 18px; }
  .slide-arrow.next { right: 18px; }

  .slider-dots { position: absolute; left: 526px; top: 516px; display: flex; gap: 14px; }
  .slider-dots span { width: 14px; height: 14px; border-radius: 50%; background: #1c1a1a; }
  .slider-dots span.current { background: var(--lime); }

  .about { position: absolute; left: 122px; top: 555px; width: 580px; }
  .about-heading { display: flex; align-items: flex-end; gap: 9px; height: 38px; font-family: 'Roboto Condensed', sans-serif;
    font-size: 26px; color: var(--ink); text-transform: uppercase; }
  .about-heading .mark { width: 20px; height: 20px; background: var(--lime); margin-bottom: 6px; margin-left: 2px; }
  .about-heading .light { font-weight: 300; }
  .about-heading strong { font-weight: 700; }
  .about-lead { margin-top: 14px; font-size: 18px; line-height: 24px; color: var(--crimson); }
  .about-body { margin-top: 9px; width: 540px; font-size: 14px; line-height: 24.5px; color: var(--text); }

  .footer-links { position: absolute; left: 122px; top: 835px; width: 576px; border-top: 1px solid var(--rule); }
  .footer-links ul { list-style: none; position: relative; height: 40px; }
  .footer-links li { position: absolute; top: 19px; font-family: 'Montserrat', sans-serif; font-weight: 500; font-size: 13px;
    color: var(--ink); display: flex; align-items: center; gap: 5px; white-space: nowrap; }
  .footer-links svg { display: block; }

  .news { position: absolute; left: 728px; top: 545px; width: 355px; height: 345px;
    background: linear-gradient(90deg, rgba(0,0,0,0.08), rgba(0,0,0,0) 14px); }
  .news-tab { position: absolute; left: 2px; top: 13px; width: 238px; height: 39px; padding-left: 30px;
    background: linear-gradient(90deg, #f1f44c, var(--lime) 60%, #e7ec3e); box-shadow: 0 2px 3px rgba(0,0,0,0.35);
    font-family: 'Roboto Condensed', sans-serif; font-size: 24px; line-height: 39px; color: var(--crimson); text-transform: uppercase; }
  .news-list { position: absolute; left: 39px; top: 70px; list-style: none; }
  .news-list li { height: 64px; }
  .news-list time { display: block; font-weight: 700; font-size: 12px; color: var(--crimson); letter-spacing: 0.4px; line-height: 14px; }
  .news-list p { font-size: 12px; line-height: 16px; color: var(--text); width: 292px; margin-top: 3px; }

  .site-footer { position: absolute; left: 121px; top: 898px; width: 960px; border-top: 1px solid var(--rule);
    text-align: center; padding-top: 16px; font-size: 12px; color: var(--text); }
</style>
</head>
<body>
  <header class="site-header">
    <div class="brand"><span class="brand-mark"></span>Calvrex Media</div>
    <span class="brand-pointer"></span>
    <p class="tagline">SITE-SPECIFIC CAMPAIGNS AT RON PRICES</p>
    <nav class="main-nav">
      <a href="#">BEAUTY</a>
      <a href="#" class="active-sep">COOKING</a>
      <a href="#">PARENTING</a>
      <a href="#">ENTERTAINMENT</a>
      <a href="#">VIDEO</a>
      <a href="#">CPC</a>
    </nav>
  </header>

  <div class="hero-band"></div>

  <section class="slider">
    <h2 class="slide-title">COOKING</h2>
    <p class="slide-sub">SITE SPECIFIC CAMPAIGNS<br>AT RON PRICES</p>
    <div class="slide-photo" role="img" aria-label="Photo of a smiling chef in white uniform holding a plate of salad and grilled food"></div>
    <svg class="slide-arrow prev" width="30" height="50" viewBox="0 0 30 50"><path d="M24 2 L8 25 L24 48 L16 48 L2 25 L16 2 Z" fill="#1c1a1a"/></svg>
    <svg class="slide-arrow next" width="30" height="50" viewBox="0 0 30 50"><path d="M6 2 L22 25 L6 48 L14 48 L28 25 L14 2 Z" fill="#1c1a1a"/></svg>
  </section>

  <div class="slider-dots">
    <span></span><span class="current"></span><span></span><span></span><span></span><span></span>
  </div>

  <section class="about">
    <h2 class="about-heading"><span class="mark"></span><span class="light">About</span> <strong>Calvrex Media</strong></h2>
    <p class="about-lead">Lorem ipsum dolor sit amet, consectetur adipiscing elit. Mauris dignissim nulla pharetra risus iaculis at consequat turpis vulputate.</p>
    <p class="about-body">Sed scelerisque magna ut quam scelerisque dictum. Morbi purus quam, sodales id vehicula non, ultricies vitae justo. Vivamus sed augue ut elit dapibus adipiscing vel in elit. Mauris adipiscing, elit a laoreet eleifend, orci lacus condimentum enim, vitae venenatis enim velit ac dolor. Nullam augue mauris, tincidunt et bibendum nec, consequat ut dui. Sed id ante in purus vulputate adipiscing ac non justo. Nulla libero sem, venenatis in fringilla pulvinar, ornare ac diam.</p>
  </section>

  <nav class="footer-links">
    <ul>
      <li style="left:-2px">ABOUT US <svg width="12" height="10" viewBox="0 0 12 10"><path d="M0 5H10M6 1L10 5L6 9" stroke="#c0202f" stroke-width="2" fill="none"/></svg></li>
      <li style="left:108px">CONTACT US <svg width="12" height="10" viewBox="0 0 12 10"><path d="M0 5H10M6 1L10 5L6 9" stroke="#c0202f" stroke-width="2" fill="none"/></svg></li>
      <li style="left:241px">MANAGEMENT TEAM <svg width="12" height="10" viewBox="0 0 12 10"><path d="M0 5H10M6 1L10 5L6 9" stroke="#c0202f" stroke-width="2" fill="none"/></svg></li>
      <li style="left:421px">NEWS <svg width="12" height="10" viewBox="0 0 12 10"><path d="M0 5H10M6 1L10 5L6 9" stroke="#c0202f" stroke-width="2" fill="none"/></svg></li>
      <li style="left:503px">CAREERS <svg width="16" height="10" viewBox="0 0 16 10"><path d="M4 5H14M10 1L14 5L10 9" stroke="#c0202f" stroke-width="2" fill="none"/></svg></li>
    </ul>
  </nav>

  <aside class="news">
    <h2 class="news-tab">Calvrex News</h2>
    <ul class="news-list">
      <li><time>JANUARY 15, 2011</time><p>Calvrex Media&nbsp; unveils new web site design and digital strategy</p></li>
      <li><time>DECEMBER 22, 2010</time><p>Calvrex Media featured in Venturist.com as one of the fastest grown online ad agencies.</p></li>
      <li><time>NOVEMBER 15, 2010</time><p>As RTB Goes Mainstream, Display Services Try To Pull Publishers Along</p></li>
      <li><time>NOVEMBER 9, 2010</time><p>Morbi purus quam, sodales id vehicula non, ultricies vitae justo</p></li>
    </ul>
  </aside>

  <footer class="site-footer">Copyright 2011 Calvrex Media. All Rights Reserved</footer>
</body>
</html>
```